Vossmer Collective - Business Card Design

several yrs ago
i have been one of the top 40 pellham photographers

when my fellow photo friends tried to join Pellham Visuals they were all rejected

Pellham Visuals told me if i formed some type of umbrella company of selected photographers they would offer me a contract as long as the portfolio images are stock worthy

so-i started the Vossmer Collective originally just for my friends and family and then grow the company to a few hundred photographers

after 4 yrs of working out all the bugs out
i will be offering other photographers to join the Vossmer Collective
------------

I now need a pro business card — retina website — an info pack about the Vossmer Collective

i bought the logo design from — https://www.markfoundry-example.com

i look at this logo as a group of independent silver balls with orange balls forming a larger group
- the Vossmer Collective
a group of independent members that will have their images sold thru Pellham Visuals - the worlds largest stack agency — under the Vossmer Collective name
--------

the look of the shadows and highlights in the logo

I want the fonts to have the similar look when it works

use the exact shade of orange and silver
I would like another to be the minor color ?

a contributor to Pellham Visuals - i want to really communicate this info
it makes my no name bus into something

please do not continue with this project

this project is on hold

in no order - information that should be part of the design - the most important part of the card - the bus name - VOSSMER COLLECTIVE - under Vossmer Collective you should have a creative tag line A contributor to Pellham Visuals - i like to see a 3d effect - refer to the website where i bought the logo - https://www.markfoundry-example.com - i included the Brink font that we used for the Vossmer Collective - incorporate this only if it helps the design - card stock - please include something other than wht - i have always liked a subtle translucent for background - only horizontal designs - one side of the card should have the logo and tag line together - use the symbols for phone mail etc.. - note the " i " in Vossmer Collective should be the same shade of orange - my card should have on this info - morris vossmer /founder / 717 555 0143 / website / email other card - tessa orbanek - her info is in the orig brief

Reason: this is my first time i have used a online site for design - only a few of the designs have the correct info none of the designs used the font that was included “brink” no one submitted a 3d feel to the designs - i need the card to have that Wow effect I just sent a more detailed brief to everyone thank you morris

Please - No more submissions

Target Market(s)

pro photographers and enthusiast

Industry/Entity Type

Business

Contact Information for Business Card

1. morris vossmer / founder -
2. tessa orbanek - 3. leon taverly
- i will add more names later

company - VOSSMER collective - tag line under logo? - in a script font - " a contributor to pellham visuals"

1. mv - no address for me

2. to - 418 E. 7th Street. Lower Marsden, NJ 08519. 609.555.0187. orbanek@inboxmail-example.com

I have several examples of what we started using their templates

Requirements
Must have
• the shadows and highlights in the logo

fonts to have the similar look when it works

Another color to be a minor color ?

i want this phrase to be included in the company name — "a contributor to Pellham Visuals"

it needs to be next to — floating around the logo — under the Vossmer Collective name anyway connecting it to the Vossmer Collective name
Nice to have
• i hope the folder names are somewhere attached to each file - if not - i will need review each file so you can understand what folder they belong to make sense of each file

i hope you get what i am trying to say
Should not have
• no address for morris vossmer

```html
<!DOCTYPE html>
<html lang="en">
<head>
<meta charset="utf-8">
<title>Vossmer Collective – Business Card</title>
<link rel="stylesheet" href="https://fonts.googleapis.com/css2?family=Exo+2:wght@400;600;700&family=Pinyon+Script&display=swap">
<style>
  :root {
    --page-bg: #ffffff;
    --card-light-top: #e9e9ea;
    --card-light-bottom: #fbfbfb;
    --orange: #f04e1e;
    --orange-light: #f7911f;
    --orange-deep: #e5361f;
    --silver: #c9ccd1;
    --graphite: #4a4c50;
    --grey-text: #55575b;
    --card-shadow: rgba(0, 0, 0, 0.18);
  }
  * { box-sizing: border-box; margin: 0; padding: 0; }
  html, body {
    width: 1200px;
    height: 900px;
    overflow: hidden;
    background: var(--page-bg);
  }
  .canvas {
    position: relative;
    width: 1200px;
    height: 900px;
    display: flex;
    align-items: center;
    justify-content: center;
    gap: 40px;
  }
  .card {
    position: relative;
    width: 525px;
    height: 300px;
    border-radius: 18px;
    overflow: hidden;
    box-shadow: 0 14px 30px var(--card-shadow);
  }

  /* Front: personal details */
  .card--front {
    background: linear-gradient(180deg, var(--card-light-top) 0%, var(--card-light-bottom) 70%);
  }
  .brand {
    position: absolute;
    display: flex;
    align-items: center;
    gap: 10px;
  }
  .brand__dot {
    flex: none;
    border-radius: 50%;
    background: var(--orange);
  }
  .brand__name {
    font-family: "Exo 2", sans-serif;
    font-weight: 700;
    letter-spacing: 0.04em;
    line-height: 1;
  }
  .card--front .brand { left: 26px; top: 126px; }
  .card--front .brand__dot { width: 18px; height: 18px; }
  .card--front .brand__name { font-size: 21px; color: var(--graphite); }

  .holder {
    position: absolute;
    right: 30px;
    top: 26px;
    text-align: right;
    font-family: "Exo 2", sans-serif;
  }
  .holder__name {
    font-size: 19px;
    font-weight: 600;
    color: var(--orange);
    letter-spacing: 0.03em;
  }
  .holder__role {
    font-size: 15px;
    color: var(--grey-text);
    letter-spacing: 0.05em;
    margin-top: 2px;
  }
  .contact {
    position: absolute;
    left: 22px;
    bottom: 34px;
    list-style: none;
    font-family: "Exo 2", sans-serif;
    font-size: 15px;
    color: var(--grey-text);
    letter-spacing: 0.03em;
  }
  .contact__item {
    display: flex;
    align-items: center;
    gap: 6px;
    line-height: 22px;
  }
  .contact__icon { width: 13px; height: 13px; fill: var(--orange); }

  /* Back: brand and tagline */
  .card--back {
    background: linear-gradient(100deg, var(--orange-light) 0%, var(--orange) 55%, var(--orange-deep) 100%);
  }
  .card__pattern {
    position: absolute;
    inset: 0;
    background: radial-gradient(ellipse at 75% 35%, rgba(255, 200, 120, 0.25), rgba(255, 200, 120, 0) 60%);
  }
  .card--back .brand {
    left: 50%;
    top: 118px;
    transform: translateX(-50%);
    white-space: nowrap;
  }
  .card--back .brand__dot { width: 20px; height: 20px; background: var(--silver); }
  .card--back .brand__name { font-size: 26px; color: #f4f4f5; }
  .tagline {
    position: absolute;
    left: 0;
    right: 0;
    top: 212px;
    text-align: center;
    font-family: "Pinyon Script", cursive;
    font-size: 22px;
    letter-spacing: 0.32em;
    color: #f6c39a;
  }
</style>
</head>
<body>
  <main class="canvas">
    <section class="card card--front" aria-label="Business card front">
      <div class="brand">
        <span class="brand__dot"></span>
        <span class="brand__name">VOSSMER COLLECTIVE</span>
      </div>
      <div class="holder">
        <p class="holder__name">Morris Vossmer</p>
        <p class="holder__role">founder</p>
      </div>
      <ul class="contact">
        <li class="contact__item">
          <svg class="contact__icon" viewBox="0 0 24 24" aria-hidden="true"><path d="M6.6 10.8a15.1 15.1 0 0 0 6.6 6.6l2.2-2.2a1 1 0 0 1 1-.25 11.4 11.4 0 0 0 3.6.57 1 1 0 0 1 1 1V20a1 1 0 0 1-1 1A17 17 0 0 1 3 4a1 1 0 0 1 1-1h3.5a1 1 0 0 1 1 1c0 1.25.2 2.45.57 3.57a1 1 0 0 1-.25 1z"/></svg>
          609.555.0187.
        </li>
        <li class="contact__item">
          <svg class="contact__icon" viewBox="0 0 24 24" aria-hidden="true"><path d="M2 5h20v14H2z M2 5l10 8 10-8" stroke="#fff" stroke-width="1.5"/></svg>
          orbanek@inboxmail-example.com
        </li>
      </ul>
    </section>

    <section class="card card--back" aria-label="Business card back">
      <div class="card__pattern" role="img" aria-label="Soft orange field of receding oval dots"></div>
      <div class="brand">
        <span class="brand__dot"></span>
        <span class="brand__name">VOSSMER COLLECTIVE</span>
      </div>
      <p class="tagline">a contributor to pellham visuals</p>
    </section>
  </main>
</body>
</html>
```